Seriöses Webdesign für innovatives Ingenieurbüro mit dem Schwerpunkt Eisenbahn Leit- und Sicherungstechnik
Zielgruppe
Die Webseite hat in erster Linie die Aufgabe zu informieren: An erster Stelle steht die Kontaktaufnahme und der Kompetenzbereich des Ingenieurbüros.
Folgende Kernkompetenzen sollen durch die Webseite transportiert werden:
Hardware-Entwicklung
Software-Entwicklung
Erneuerung alter Techniken
Begutachtung
Software für Lieferantenbewertung
Störungsmanagement(system)
Zielgruppe:
Die Webseite soll als Online-Visitenkarte für bestehende und neue Kontakte dienen. Gerade neue (Messe-)Kontakte erleben die Webseite als erste Anlaufstelle und erhalten einen Einblick in das vorhandene Leistungsspektrum des Ingenieurbüros und die Möglichkeiten der Kontaktaufnahme.

```html
<!DOCTYPE html>
<html lang="de">
<head>
<meta charset="utf-8">
<title>Spurwerk – Ingenieurbüro für Leit- und Sicherungstechnik</title>
<link href="https://fonts.googleapis.com/css2?family=Arimo:wght@400;700&display=swap" rel="stylesheet">
<style>
  :root {
    --brand-blue: #008bbd;
    --accent-orange: #e0561f;
    --text-dark: #3a3a3a;
    --band-blue: #cbdbe5;
    --band-pattern: #bfd1dc;
    --white: #ffffff;
  }
  * { margin: 0; padding: 0; box-sizing: border-box; }
  html, body { width: 1130px; height: 1200px; overflow: hidden; background: var(--white); }
  body { position: relative; font-family: "Arimo", Arial, sans-serif; color: var(--text-dark); }

  .site-header {
    position: absolute; left: 150px; top: 0; width: 980px; height: 44px;
    background: var(--brand-blue); color: var(--white);
  }
  .brand-name {
    position: absolute; left: 163px; top: 9px;
    font-size: 24px; font-weight: 700; letter-spacing: 0.5px;
  }
  .contact-line {
    position: absolute; left: 587px; top: 19px;
    display: flex; align-items: center; gap: 24px;
    font-size: 13px; white-space: nowrap;
  }
  .contact-phone { display: flex; align-items: center; gap: 3px; }
  .contact-phone svg { width: 9px; height: 13px; flex: none; }

  .hero {
    position: absolute; left: 150px; top: 44px; width: 980px; height: 202px;
    background: linear-gradient(100deg, #6d6a68 0%, #8a8683 30%, #b9b7b5 45%, #7b7572 65%, #5f5651 100%);
  }

  .service-nav { position: absolute; left: 313px; top: 278px; list-style: none; }
  .service-nav li { height: 27px; }
  .service-nav a {
    color: var(--brand-blue); text-decoration: none;
    font-size: 10.5px; font-weight: 700;
  }

  .text-block { position: absolute; left: 559px; width: 352px; }
  .text-block h1, .text-block h2 {
    color: var(--accent-orange); font-size: 18px; font-weight: 700; margin-bottom: 9px;
  }
  .lead { font-size: 12.2px; font-weight: 700; line-height: 20px; margin-bottom: 20px; }
  .body-copy { font-size: 11.3px; line-height: 20px; white-space: nowrap; }

  .intro { top: 278px; }

  .feature-band {
    position: absolute; left: 150px; top: 480px; width: 980px; height: 386px;
    background: var(--band-blue);
  }
  .track-diagram {
    position: absolute; inset: 0;
    background: linear-gradient(90deg, var(--band-blue) 0%, var(--band-pattern) 40%, var(--band-pattern) 70%, var(--band-blue) 100%);
    opacity: 0.6;
  }
  .signal-photo {
    position: absolute; left: 815px; top: 45px; width: 82px; height: 124px;
    background: linear-gradient(180deg, #a9b3b8 0%, #6e6a5e 45%, #4f4538 100%);
  }
  .feature { top: 646px; }

  .control-room-photo {
    position: absolute; left: 313px; top: 939px; width: 164px; height: 122px;
    background: linear-gradient(135deg, #cfd2c8 0%, #a9aea3 40%, #5b5b57 100%);
  }
  .closing { top: 932px; }

  .site-footer {
    position: absolute; left: 149px; top: 1156px; width: 981px; height: 44px;
    background: var(--brand-blue);
  }
  .footer-nav { position: absolute; left: 408px; top: 14px; display: flex; list-style: none; }
  .footer-nav a {
    color: var(--white); text-decoration: none; font-size: 10.5px; font-weight: 700; margin-right: 35px;
  }
</style>
</head>
<body>
  <header class="site-header">
    <div class="brand-name">Spurwerk</div>
    <div class="contact-line">
      <span class="contact-mail">info@spurwerk.com</span>
      <span class="contact-phone">
        <svg viewBox="0 0 9 13" aria-hidden="true"><path d="M3 0.5 L5 0.5 L5 3.5 L3.5 4.5 C3 6.5 3 7.5 3.5 8.5 L5 9.5 L5 12.5 L3 12.5 C0.5 10 0.5 3 3 0.5 Z" fill="#fff"/></svg>
        <span>0170 31 64 29</span>
      </span>
    </div>
  </header>

  <div class="hero" role="img" aria-label="Foto: Hochgeschwindigkeitszug auf Gleisanlage mit Oberleitungsmasten"></div>

  <nav>
    <ul class="service-nav">
      <li><a href="#">Hardware-Entwicklung</a></li>
      <li><a href="#">Software-Entwicklung</a></li>
      <li><a href="#">Erneuerung alter Techniken</a></li>
      <li><a href="#">Begutachtung</a></li>
      <li><a href="#">Software für Lieferantenbewertung</a></li>
      <li><a href="#">Störungsmanagementsystem</a></li>
    </ul>
  </nav>

  <section class="text-block intro">
    <h1>Dies ist ein Typoblindtext</h1>
    <p class="lead">An ihm kann man sehen, ob alle Buchstaben da sind und wie sie aussehen. Manchmal benutzt man Worte wie Hamburgefonts, oder Handgloves, um Schriften zu testen.</p>
    <p class="body-copy">Manchmal Sätze, die alle Buchstaben des Alphabets enthalten -<br>man nennt diese Sätze »Pangrams«. Sehr bekannt ist dieser:<br>The quick brown fox jumps over the lazy old dog.</p>
  </section>

  <section class="feature-band">
    <div class="track-diagram" role="img" aria-label="Dezent geprägter Gleisplan eines Stellwerks als Hintergrund"></div>
    <div class="signal-photo" role="img" aria-label="Foto: Signalanlage an einem Gleis"></div>
  </section>
  <section class="text-block feature">
    <h2>Ein Typoblindtext</h2>
    <p class="lead">An ihm kann man sehen, ob alle Buchstaben da sind und wie sie aussehen. Manchmal benutzt man Worte.</p>
    <p class="body-copy">Manchmal Sätze, die alle Buchstaben des Alphabets enthalten -<br>man nennt diese Sätze »Pangrams«. Sehr bekannt ist dieser:<br>The quick brown fox jumps over the lazy old dog.<br>Sehr bekannt ist dieser: The quick brown fox jumps over the lazy dog.<br>The quick brown fox jumps over the lazy old dog.</p>
  </section>

  <div class="control-room-photo" role="img" aria-label="Foto: Stellwerksraum mit Stelltafel und Uhr"></div>
  <section class="text-block closing">
    <p class="lead">An ihm kann man sehen, ob alle Buchstaben da sind und wie sie aussehen. Manchmal benutzt man Worte wie Hamburgefonts, oder Handgloves, um Schriften zu testen.</p>
    <p class="body-copy">Manchmal Sätze, die alle Buchstaben des Alphabets enthalten -<br>man nennt diese Sätze »Pangrams«. Sehr bekannt ist dieser:<br>The quick brown fox jumps over the lazy old dog.<br>Man nennt diese Sätze »Pangrams«. Sehr bekannt ist dieser:<br>The quick brown fox jumps over the lazy old dog.</p>
  </section>

  <footer class="site-footer">
    <ul class="footer-nav">
      <li><a href="#">Impressum</a></li>
      <li><a href="#">Datenschutz</a></li>
      <li><a href="#">Hilfe</a></li>
      <li><a href="#">Copyright</a></li>
      <li><a href="#">Sprache ändern</a></li>
    </ul>
  </footer>
</body>
</html>
```